Local Real Estate Office needs an innovative Letterhead Design

Using the attached Logo, please create a letterhead design that is innovative and unusual. I am looking for something that will appeal to young homebuyers as well as seniors going into Condos.

The attached logo for Marrowfield Estates needs to be included (small but readable) as well as spaces for 2 agents "head shots" photos.
Updates

I need a spot on the letterhead for two photos (head shots). thx

Industry/Entity Type

Real Estate

```html
<!DOCTYPE html>
<html lang="en">
<head>
<meta charset="utf-8">
<title>Northridge Homes Letterhead</title>
<link href="https://fonts.googleapis.com/css2?family=Arimo:wght@400;700&display=swap" rel="stylesheet">
<style>
  :root {
    --brand-blue: #1638d8;
    --brand-blue-deep: #0f2bb8;
    --brand-blue-light: #3f66f0;
    --accent-orange: #f08a1c;
    --accent-yellow: #f6c300;
    --ink: #1a1a1a;
    --rule: #555555;
    --frame: #2a2a2a;
    --paper: #ffffff;
    --badge-navy: #14306e;
  }
  * { margin: 0; padding: 0; box-sizing: border-box; }
  html, body { width: 849px; height: 1200px; overflow: hidden; background: var(--paper); }
  .letterhead {
    position: relative;
    width: 849px;
    height: 1200px;
    background: var(--paper);
    font-family: "Arimo", Arial, sans-serif;
    color: var(--ink);
    overflow: hidden;
  }
  .header-swoosh { position: absolute; top: 0; left: 0; width: 849px; height: 150px; }
  .brand-name {
    position: absolute;
    top: 16px;
    left: 60px;
    color: var(--paper);
    font-weight: 700;
    line-height: 1;
    text-align: center;
  }
  .brand-name .brand-main { display: block; font-size: 28px; letter-spacing: -0.5px; }
  .brand-name .brand-sub { display: block; font-size: 13px; letter-spacing: 2px; margin-top: 4px; }
  .contact-block {
    position: absolute;
    top: 78px;
    right: 235px;
    text-align: right;
    font-size: 15px;
    line-height: 17.5px;
  }
  .agent-photos { position: absolute; top: 48px; left: 627px; display: flex; gap: 5px; }
  .agent-photo {
    width: 68px;
    height: 81px;
    border: 1.5px solid var(--frame);
    border-radius: 6px;
  }
  .agent-photo.agent-senior { background: linear-gradient(180deg, #d9d9d9 0%, #c9a89a 45%, #3a3f48 100%); }
  .agent-photo.agent-junior { background: linear-gradient(180deg, #e6e6e6 0%, #d2b09c 45%, #2f3138 100%); }
  .header-rule {
    position: absolute;
    top: 141px;
    left: 0;
    width: 765px;
    height: 1px;
    background: var(--rule);
  }
  .office-badge {
    position: absolute;
    top: 1137px;
    left: 767px;
    width: 57px;
    height: 40px;
    background: var(--badge-navy);
    border: 1px solid #c8cdd8;
    color: var(--paper);
    font-weight: 700;
    font-size: 9px;
    line-height: 10px;
    text-align: center;
    display: flex;
    align-items: center;
    justify-content: center;
    padding: 2px;
  }
  .footer-band {
    position: absolute;
    bottom: 0;
    left: 0;
    width: 849px;
    height: 18px;
    background: linear-gradient(90deg, var(--brand-blue-deep), var(--brand-blue), var(--brand-blue-light));
  }
</style>
</head>
<body>
  <div class="letterhead">
    <svg class="header-swoosh" viewBox="0 0 849 150" aria-hidden="true">
      <defs>
        <linearGradient id="swoosh-fill" x1="0" y1="0" x2="1" y2="0">
          <stop offset="0" stop-color="#0f2bb8"/>
          <stop offset="0.5" stop-color="#1a3ee0"/>
          <stop offset="1" stop-color="#2a55f2"/>
        </linearGradient>
      </defs>
      <path d="M0,0 H849 V102 C820,42 760,16 680,11 C520,4 300,40 150,82 C90,100 40,122 0,140 Z" fill="url(#swoosh-fill)"/>
      <path d="M150,82 C300,40 480,10 650,10" fill="none" stroke="var(--accent-orange)" stroke-width="2"/>
      <path d="M650,10 C745,10 812,42 849,108" fill="none" stroke="var(--accent-yellow)" stroke-width="5"/>
    </svg>

    <div class="brand-name">
      <span class="brand-main">Northridge</span>
      <span class="brand-sub">HOMES.COM</span>
    </div>

    <address class="contact-block" style="font-style: normal;">
      <div class="contact-phone">Phone: 306-555-0148</div>
      <div class="contact-fax">Fax: (306) 555-0172</div>
      <div class="contact-web">www.NorthridgeHomes.com</div>
    </address>

    <div class="agent-photos">
      <div class="agent-photo agent-senior" role="img" aria-label="Head shot of senior agent"></div>
      <div class="agent-photo agent-junior" role="img" aria-label="Head shot of junior agent"></div>
    </div>

    <div class="header-rule"></div>

    <div class="office-badge">Marrowfield Estates</div>

    <div class="footer-band"></div>
  </div>
</body>
</html>
```